Corvane Edge Supplies - Stone Tooling Company

We need a round design for a saw blade that cuts stone.

We provide the tools and equipment necessary to cut, shape, polish granite-marble-engineered stone for your home.

Think designs on a skateboard wheel. Urban-street designs. We like something along the lines of something similar to the wheels on larkhollowrolls.com, snowboard designs etc..

2 Colors. Background - Matte Black. Gold print on top.
No shading/gradient as this has to be solid colors black/gold.
We would like the following text imbedded somewhere-
"Approved by Tall Morris"
"Granite/Engineered Stone"

Must have logo thats in the file

Target Market(s)

granite countertop fabricators- current designs are boring- we want this to stand out.

Industry/Entity Type

It Company

Font styles to use
Sans Serif
Decorative

Requirements
Must have
• Check attached picture. Something similar except with our attached logo, black background, and gold print.
Nice to have
• urban, street, skate, surf, tattoo, style
Should not have
• shadowing, unless by dots and lines for silk screen printing.

```html
<!DOCTYPE html>
<html lang="en">
<head>
<meta charset="utf-8">
<title>Corvane Edge Supplies – Stone Blade Print</title>
<link rel="stylesheet" href="https://fonts.googleapis.com/css2?family=Montserrat:wght@600;800&display=swap">
<style>
  :root {
    --backdrop: #e9e6e1;
    --blade-steel: #c4c6c8;
    --blade-steel-dark: #8d9092;
    --matte-black: #050505;
    --gold: #d9b23a;
  }
  html, body {
    margin: 0;
    padding: 0;
    width: 1200px;
    height: 1200px;
    overflow: hidden;
    background: var(--backdrop);
  }
  .blade {
    display: block;
    width: 1200px;
    height: 1200px;
  }
  .blade-teeth {
    fill: none;
    stroke: var(--blade-steel);
    stroke-width: 74;
    stroke-dasharray: 8.6 1.4;
  }
  .tooth-edge {
    fill: none;
    stroke: var(--blade-steel-dark);
    stroke-width: 74;
    stroke-dasharray: 8.6 1.4;
    stroke-dashoffset: 0;
    opacity: 0.35;
  }
  .tooth-slot {
    fill: none;
    stroke: var(--matte-black);
    stroke-width: 3;
    stroke-dasharray: 0.15 9.85;
    stroke-dashoffset: -9.3;
  }
  .blade-face { fill: var(--matte-black); }
  .swirl-graphic { fill: var(--gold); }
  .arbor-ring { fill: var(--blade-steel); stroke: var(--blade-steel-dark); stroke-width: 3; }
  .arbor-hole { fill: var(--backdrop); }
  .brand-mark { fill: var(--gold); }
  .brand-name {
    font-family: "Montserrat", sans-serif;
    font-weight: 800;
    font-size: 135px;
    fill: var(--gold);
  }
  .endorsement {
    font-family: "Montserrat", sans-serif;
    font-weight: 800;
    font-size: 64px;
    fill: var(--gold);
  }
  .material-line {
    font-family: "Montserrat", sans-serif;
    font-weight: 800;
    font-size: 28px;
    fill: var(--gold);
  }
</style>
</head>
<body>
<svg class="blade" viewBox="0 0 1200 1200" xmlns="http://www.w3.org/2000/svg">
  <defs>
    <path id="brand-arc" d="M392.2,480 A240,240 0 0 1 825.5,682.1"/>
    <path id="endorsement-arc" d="M928.9,719.7 A350,350 0 0 1 255.3,660.8"/>
    <path id="material-arc" d="M814.5,780 A280,280 0 0 1 385.5,780"/>
  </defs>

  <circle class="blade-teeth" cx="600" cy="600" r="475" pathLength="480"/>
  <circle class="tooth-slot" cx="600" cy="600" r="420" pathLength="480"/>
  <circle class="blade-face" cx="600" cy="600" r="440"/>

  <circle class="swirl-graphic" cx="600" cy="600" r="195" role="img"
          aria-label="Gold swirl of curved blade shapes spinning around the arbor hole"/>

  <circle class="arbor-ring" cx="600" cy="600" r="72"/>
  <circle class="arbor-hole" cx="600" cy="600" r="60"/>

  <circle class="brand-mark" cx="268" cy="580" r="46"/>

  <text class="brand-name">
    <textPath href="#brand-arc" startOffset="8" textLength="695" lengthAdjust="spacing">Corvane</textPath>
  </text>

  <text class="material-line">
    <textPath href="#material-arc" startOffset="50%" text-anchor="middle">Granite / Engineered Stone</textPath>
  </text>

  <text class="endorsement">
    <textPath href="#endorsement-arc" startOffset="50%" text-anchor="middle">Approved by Tall Morris</textPath>
  </text>
</svg>
</body>
</html>
```